Bourbon label design for bourbon brand. Looking to freshen our current label.

I need a Bourbon label design for our rebranded Bourbon bottle. Label should include picture of our horse and our logo on the bottle. Front Label is 3.5 inches wide and 6 inches tall, back label is 4 inches tall and 3 inches wide. Back label can be a simple plain logo like the one in the brief. I have included a design of our current bottle and label. We want to stay close to the current color schemes but want a fresh rebrand of the design. The label needs to be the correct size on a tall bottle like pictured.

Target Market(s)

Our Bourbon members, 30-50 year old males

Requirements
Must have
• Picture of our horse, our B logo , straight Bourbon whiskey on the front. Room to edit text on the back label.

```html
<!DOCTYPE html>
<html lang="en">
<head>
<meta charset="utf-8">
<title>Ironside Straight Bourbon Whiskey – Front and Back Label</title>
<link href="https://fonts.googleapis.com/css2?family=Oswald:wght@500;600;700&family=Space+Grotesk:wght@400;500;600;700&family=Archivo:wght@600&display=swap" rel="stylesheet">
<style>
  :root {
    --canvas-light: #eceeed;
    --canvas-grey: #8a8a8a;
    --label-black: #0b0b0b;
    --gold-deep: #b58a3c;
    --gold-light: #f1e39a;
    --gold-flat: #d9bd6a;
    --white: #ffffff;
    --ink: #1f1f1f;
    --paper: #f4f4f4;
  }
  * { margin: 0; padding: 0; box-sizing: border-box; }
  html, body { width: 1200px; height: 1035px; overflow: hidden; }
  body { position: relative; background: var(--canvas-light); }

  .panel-grey { position: absolute; left: 600px; top: 0; width: 600px; height: 1035px; background: var(--canvas-grey); }

  /* Front label */
  .front-label {
    position: absolute; left: 50px; top: 88px; width: 500px; height: 859px;
    background: var(--label-black); overflow: hidden;
    font-family: "Oswald", sans-serif; color: var(--white);
  }
  .front-photo {
    position: absolute; inset: 0;
    background:
      radial-gradient(ellipse 65% 40% at 35% 25%, rgba(120,120,120,.6), rgba(80,80,80,.3) 60%, transparent 85%),
      linear-gradient(180deg, #4a4a4a 0%, #3a3a3a 35%, #1a1a1a 65%, #050505 100%);
  }
  .gold-band { position: absolute; left: 0; width: 500px; height: 24px; }
  .gold-band.top { top: 0; }
  .gold-band.bottom { bottom: 0; }

  .mark-circle {
    position: absolute; left: 200px; top: 178px; width: 100px; height: 100px;
    border: 3px solid var(--white); border-radius: 50%;
  }
  .brand-name {
    position: absolute; left: 0; top: 312px; width: 500px; text-align: center;
    font-weight: 700; font-size: 104px; line-height: 1; letter-spacing: 0;
    color: var(--gold-flat);
  }
  .spirit-type {
    position: absolute; left: 0; top: 436px; width: 500px; text-align: center;
    font-weight: 600; font-size: 26px; line-height: 1; letter-spacing: -.2px;
  }
  .feature-frame { position: absolute; left: 164px; top: 508px; width: 172px; height: 141px; }
  .feature { position: absolute; left: 0; width: 500px; text-align: center; font-weight: 600; font-size: 23px; line-height: 1; }
  .feature.single { top: 540px; }
  .feature.cask { top: 592px; }

  .spec-label { position: absolute; top: 770px; width: 86px; font-family: "Archivo", sans-serif; font-weight: 600; font-size: 12px; line-height: 12px; text-align: center; }
  .spec-box { position: absolute; top: 788px; width: 86px; height: 22px; background: var(--white); color: var(--ink); font-family: "Archivo", sans-serif; font-weight: 600; font-size: 11.5px; line-height: 22px; text-align: right; padding-right: 8px; }

  /* Back label */
  .back-label {
    position: absolute; left: 685px; top: 232px; width: 429px; height: 572px;
    background: var(--paper); overflow: hidden;
    font-family: "Space Grotesk", sans-serif; color: var(--ink); text-align: center;
  }
  .back-photo {
    position: absolute; left: 40px; top: 20px; width: 360px; height: 552px;
    background: radial-gradient(ellipse 55% 50% at 50% 45%, rgba(190,190,190,.45), rgba(220,220,220,.2) 65%, transparent 90%);
  }
  .back-mark { position: absolute; left: 186px; top: 14px; width: 56px; height: 56px; border: 3px solid var(--ink); border-radius: 50%; }
  .back-brand { position: absolute; left: 0; top: 89px; width: 429px; font-weight: 700; font-size: 16px; line-height: 15px; }
  .back-company { position: absolute; left: 0; top: 121px; width: 429px; font-weight: 500; font-size: 6.5px; line-height: 8px; letter-spacing: 3px; }
  .edition { position: absolute; left: 0; top: 146px; width: 429px; font-weight: 600; font-size: 23px; line-height: 30.5px; }
  .story { position: absolute; left: 36px; width: 357px; font-weight: 600; font-size: 11.5px; line-height: 15.5px; }
  .story.first { top: 246px; }
  .story.second { top: 319px; }
  .producer { position: absolute; left: 0; top: 383px; width: 429px; font-weight: 600; font-size: 13px; line-height: 17px; }
  .website { position: absolute; left: 0; top: 417px; width: 429px; font-weight: 700; font-size: 20.5px; line-height: 26px; }
  .warning { position: absolute; left: 27px; top: 447px; width: 378px; font-weight: 400; font-size: 11px; line-height: 15.6px; letter-spacing: .4px; text-align: justify; }
  .volume { position: absolute; left: 0; top: 533px; width: 429px; font-weight: 700; font-size: 19px; line-height: 24px; }
</style>
</head>
<body>
  <div class="panel-grey"></div>

  <section class="front-label">
    <div class="front-photo" role="img" aria-label="Black and white photo of the racehorse and jockey"></div>

    <svg class="gold-band top" viewBox="0 0 500 24" preserveAspectRatio="none" aria-hidden="true">
      <defs>
        <linearGradient id="goldTop" x1="0" x2="1">
          <stop offset="0" stop-color="#b58a3c"/><stop offset=".45" stop-color="#f1e39a"/><stop offset="1" stop-color="#b58a3c"/>
        </linearGradient>
      </defs>
      <polygon points="0,0 500,0 500,1 0,18" fill="url(#goldTop)"/>
    </svg>

    <div class="mark-circle"></div>
    <div class="brand-name">IRONSIDE</div>
    <div class="spirit-type">STRAIGHT BOURBON WHISKEY</div>

    <svg class="feature-frame" viewBox="0 0 172 141" aria-hidden="true">
      <g stroke="#ffffff" stroke-width="1.2">
        <line x1="0" y1="16" x2="172" y2="16"/>
        <line x1="0" y1="73" x2="172" y2="73"/>
        <line x1="0" y1="124" x2="172" y2="124"/>
        <line x1="8" y1="0" x2="8" y2="141"/>
        <line x1="166" y1="0" x2="166" y2="141"/>
      </g>
    </svg>
    <div class="feature single">SINGLE BARREL</div>
    <div class="feature cask">CASK STRENGTH</div>

    <div class="spec-label" style="left:105px">ALC/VOL</div>
    <div class="spec-label" style="left:208px">AGED</div>
    <div class="spec-label" style="left:309px">BARREL NO</div>
    <div class="spec-box" style="left:105px"></div>
    <div class="spec-box" style="left:208px">Years</div>
    <div class="spec-box" style="left:309px"></div>

    <svg class="gold-band bottom" viewBox="0 0 500 24" preserveAspectRatio="none" aria-hidden="true">
      <defs>
        <linearGradient id="goldBottom" x1="0" x2="1">
          <stop offset="0" stop-color="#b58a3c"/><stop offset=".45" stop-color="#f1e39a"/><stop offset="1" stop-color="#b58a3c"/>
        </linearGradient>
      </defs>
      <polygon points="0,0 500,18 500,24 0,24" fill="url(#goldBottom)"/>
    </svg>
  </section>

  <section class="back-label">
    <div class="back-photo" role="img" aria-label="Faint photo of the racehorse and jockey"></div>
    <div class="back-mark"></div>
    <div class="back-brand">IRONSIDE<br>BARREL</div>
    <div class="back-company">COMPANY</div>
    <h1 class="edition">Winners Series<br>Silver Tempest Edition<br>Single Barrel No.45</h1>
    <p class="story first">The Ironside Racing Winners Series honors the horses who have brought home victories for our stable. This edition celebrates Silver Tempest and her maiden victory on May 28, 2021.</p>
    <p class="story second">Raise a glass to her incredible career with this non-chill filtered single barrel crafted in her honor. Here’s to Silver Tempest a true champion!</p>
    <p class="producer">Bottled by Old Riverbend Whiskey Co., Louisville, Kentucky<br>Distilled in Bardstown. Kentucky</p>
    <p class="website">IRONSIDE-GROUP.COM</p>
    <p class="warning">GOVERNMENT WARNING: (1) According to the Surgeon General, women should not drink alcoholic beverages during pregnancy because of the risk of birth defects. (2) Consumption of alcoholic beverages impairs your ability to drive a car or operate machinery, and may cause health problems.</p>
    <p class="volume">750ML</p>
  </section>
</body>
</html>
```